依頼詳細
■入れてほしい文言
エクセルデータ参照してください

■ のぼり、ポスターサイズ情報
サイズ:横600mm×縦1800mm以内

■ デザインへの要望
洋風調、和風調 のぼりデザインを作成したい
デザイン参考に添付ファイルの画像を参照
記載項目
サイズ:横600mm×縦1800mm以内
希望イメージ
シンプル 複雑
単色 カラフル
暗い 明るい
日常 高級
遊び心 厳粛
未来的 伝統的
女性的 男性的
希望する色
納品ファイル
• イラストレーター形式 (.ai)
• フォトショップ形式 (.psd)
• PNG形式 (.png)
補足説明

```html
<!DOCTYPE html>
<html lang="ja">
<head>
<meta charset="utf-8">
<title>青葉建具組合 のぼり</title>
<link rel="stylesheet" href="https://fonts.googleapis.com/css2?family=Kaisei+Tokumin:wght@800&family=Yuji+Syuku&display=swap">
<style>
  :root {
    --maroon: #772a2f;
    --orange: #c9591c;
    --gold: #d3950f;
    --pattern-tone: #874330;
    --white: #ffffff;
  }
  html, body {
    margin: 0;
    padding: 0;
    overflow: hidden;
  }
  .banner {
    position: relative;
    width: 1200px;
    height: 3596px;
    background: var(--maroon);
    overflow: hidden;
  }
  .backdrop {
    position: absolute;
    inset: 0;
    width: 1200px;
    height: 3596px;
  }
  .vertical {
    position: absolute;
    writing-mode: vertical-rl;
    margin: 0;
    line-height: 1;
    white-space: nowrap;
  }
  .org-name {
    left: 555px;
    top: 110px;
    font-family: "Kaisei Tokumin", serif;
    font-weight: 800;
    font-size: 430px;
    letter-spacing: 50px;
    color: var(--white);
  }
  .org-type {
    left: 690px;
    top: 2370px;
    font-family: "Kaisei Tokumin", serif;
    font-weight: 800;
    font-size: 290px;
    letter-spacing: 60px;
    color: var(--white);
  }
  .region {
    left: 70px;
    top: 620px;
    font-family: "Yuji Syuku", serif;
    font-size: 300px;
    letter-spacing: 40px;
    color: var(--gold);
  }
  .region .particle {
    font-size: 240px;
  }
  .nickname {
    left: 135px;
    top: 1660px;
    font-family: "Yuji Syuku", serif;
    font-size: 310px;
    letter-spacing: 70px;
    color: var(--maroon);
  }
</style>
</head>
<body>
<main class="banner">
  <svg class="backdrop" viewBox="0 0 1200 3596" xmlns="http://www.w3.org/2000/svg">
    <defs>
      <linearGradient id="sweep-top" x1="0" y1="0" x2="1" y2="1">
        <stop offset="0" stop-color="#d0601c"/>
        <stop offset="1" stop-color="#772a2f"/>
      </linearGradient>
      <linearGradient id="sweep-mid" x1="0" y1="0" x2="1" y2="1">
        <stop offset="0" stop-color="#772a2f"/>
        <stop offset="0.6" stop-color="#a8461f"/>
        <stop offset="1" stop-color="#c9591c"/>
      </linearGradient>
    </defs>
    <path class="sweep sweep-top" fill="url(#sweep-top)"
      d="M0 0 H1200 V120 C1000 60 760 120 560 200 C380 270 200 330 0 380 Z"/>
    <path class="sweep sweep-mid" fill="url(#sweep-mid)" opacity="0.75"
      d="M0 760 C240 640 520 520 820 560 C1000 590 1120 660 1200 720 V1500 C1060 1300 900 1200 700 1180 C460 1160 240 1240 0 1380 Z"/>
    <circle class="moon" cx="380" cy="1980" r="460" fill="var(--gold)"/>
    <rect class="gold-field" x="0" y="1980" width="840" height="820" fill="var(--gold)"/>
    <rect class="gold-band" x="840" y="2120" width="360" height="60" fill="var(--gold)"/>
    <path class="lattice-field" role="img" aria-label="麻の葉文様の和柄パターン（えんじ地に金線）"
      fill="var(--pattern-tone)"
      d="M840 2180 H1200 V3596 H0 V2800 H840 Z"/>
  </svg>

  <h1 class="vertical org-name">青葉建具</h1>
  <p class="vertical org-type">組合</p>
  <p class="vertical region">越後<span class="particle">の</span></p>
  <p class="vertical nickname">小京都</p>
</main>
</body>
</html>
```